Dynamic Lead Design (Partial WebPage)

To encourage visitors to our website to donate to our organization, we would like to replace the Dynamic Lead on our website with one that will evoke emotion from the viewer and motivate them to donate generously.

The deliverable should be a mockup of the design in context of the current website. See attached file for editable area. Fonts used in the mockup should be code-able in HTML/CSS.

The website
http://www.tumorhope.org

Please use this wireframe for reference:
http://app.wiredraftly.com/8b1c47d2e09f3a5561c7d4e0a2b9f8c3d7e61a04/7718264

Content:
[Image should evoke emotion from the viewer and motivate them to donate generously.]
Headline - “Give to HAVEN.”
Sub Headline - “Cancer patients find answers here. Your donation makes that possible.”
Call to action label - “Donate”

We love these examples:

Mt. Orwell Hearts and Sharing (http://www.hs.mtorwell.org/mtorwell/v/index.jsp?vgnextoid=7a5d21f0c3b9e4d8VgnVCM100000481726bdRCRD)
Kindly Wells (http://www.kindlywells.org/)

Design Size:
width: 971px
height: 300px

***see attached document for design area***

- Organization Background -

Our website receives over 40,000 unique visitors each month - mostly cancer patients and their family members seeking information about their disease. We would like to drive our visitors to donate to our nonprofit throughout late November and December (the majority of our donations from individuals come in during that time period).

We will be mailing an appeal letter to our database in mid-November. With this banner ad, we seek to complement that appeal. Some key messages from our appeal are:

- We focus on getting patients and their loved ones the best, most up-to-date information from trusted doctors who are leaders in cancer research – for free. We don’t sell a particular product or procedure. We simply arm them with the most current information so they can make the best decision for their own (or their loved one’s) care.

- What is the value of the support they or someone they know has received from our organization? Twenty-five dollars? One hundred dollars? One thousand? Can you even put an amount to it? Whatever it is, please consider making an end of year donation to this organization that has helped so many, comforted hundreds of thousands of patients and caretakers, and been there when needed.

- 2014 will be a year of growth. We just hired our first executive director. She is experienced in helping small nonprofits grow in size, revenue, and scope, and will undoubtedly bring a new level of energy to our work.

- In just a few months, we will hold two patient forums – first-of-its-kind programs for the organization. As we continue to grow, we will be able to offer more of these types of programs to more patients throughout the US.

Industry/Entity Type

Charity

Requirements
Must have
• - Must Adhere to existing website branding

```html
<!DOCTYPE html>
<html lang="en">
<head>
<meta charset="utf-8">
<title>HAVEN – Give to HAVEN</title>
<link href="https://fonts.googleapis.com/css2?family=Montserrat:wght@500;600;700&family=Arimo:wght@400;700&display=swap" rel="stylesheet">
<style>
  :root {
    --teal: #5cc4a0;
    --teal-soft: #bfe6d6;
    --coral: #f7907c;
    --slate: #77787b;
    --ink: #222222;
    --heading-grey: #6d6e71;
    --link-green: #14874a;
    --rule: #d9d9d9;
    --page: #ffffff;
    --blush-1: #fbe1dc;
    --blush-2: #fdf0ec;
  }
  * { box-sizing: border-box; margin: 0; padding: 0; }
  html, body { width: 1200px; height: 780px; overflow: hidden; background: var(--page); }
  body { font-family: "Arimo", Arial, sans-serif; color: var(--ink); position: relative; }

  .brand { position: absolute; left: 188px; top: 40px; display: flex; align-items: center; gap: 14px; }
  .brand-dot { width: 70px; height: 70px; border-radius: 50%; background: var(--teal); }
  .brand-name { font-family: "Montserrat", sans-serif; font-weight: 700; font-size: 34px; letter-spacing: 2px; color: var(--slate); }

  .search { position: absolute; left: 573px; top: 40px; width: 362px; height: 54px; border: 6px solid var(--teal-soft); border-radius: 28px; display: flex; align-items: center; padding: 0 12px 0 20px; gap: 4px; }
  .search-field { width: 250px; height: 22px; border: 1px solid #b9b9b9; font-size: 9px; color: #999; padding: 5px 6px; }
  .search-button { background: var(--teal-soft); font-size: 10px; font-weight: 700; padding: 6px 10px; }
  .search-clear { font-size: 12px; color: #999; margin-left: 6px; }

  .main-nav { position: absolute; left: 187px; top: 135px; width: 870px; height: 42px; display: flex; gap: 3px; }
  .nav-tab { flex: 0 0 auto; background: var(--teal); color: #fff; font-family: "Montserrat", sans-serif; font-weight: 600; font-size: 13.5px; letter-spacing: 1px; line-height: 1; text-align: center; display: flex; align-items: center; justify-content: center; flex-direction: column; white-space: nowrap; }
  .nav-tab small { font-size: 11.5px; display: block; margin-top: 2px; }
  .nav-tab.account { background: var(--slate); }
  .nav-tab.donate { background: var(--coral); border-top-right-radius: 10px; position: relative; }
  .donate-badge { position: absolute; right: 0; top: -32px; width: 52px; height: 40px; background: var(--coral); border-radius: 26px 10px 0 0; }

  .lead { position: absolute; left: 187px; top: 181px; width: 870px; height: 269px; background: linear-gradient(90deg, var(--blush-2) 0%, var(--blush-1) 55%, var(--blush-2) 100%); overflow: hidden; }
  .lead-photo { position: absolute; left: 0; top: 0; width: 430px; height: 269px; background: linear-gradient(110deg, #f4ece4 0%, #efd9cc 45%, rgba(251,225,220,0) 100%); }
  .lead-copy { position: absolute; left: 359px; top: 42px; width: 464px; text-align: center; }
  .lead-rule { height: 1px; background: var(--slate); opacity: .7; }
  .lead-title { font-family: "Montserrat", sans-serif; font-weight: 600; font-size: 42px; letter-spacing: 5px; color: var(--teal); padding: 10px 0; line-height: 46px; white-space: nowrap; }
  .lead-sub { margin-top: 26px; font-family: "Montserrat", sans-serif; font-weight: 500; font-size: 12.5px; letter-spacing: 2.2px; color: var(--slate); line-height: 17px; text-transform: uppercase; white-space: nowrap; }
  .lead-cta { position: absolute; left: 502px; top: 184px; width: 176px; height: 46px; border-radius: 10px; background: var(--coral); color: #fff; font-family: "Montserrat", sans-serif; font-weight: 700; font-size: 17px; letter-spacing: 4px; display: flex; align-items: center; justify-content: center; gap: 10px; }

  .news { position: absolute; left: 187px; top: 488px; width: 617px; }
  .share { position: absolute; left: 425px; top: 0; width: 176px; height: 17px; border: 1px solid var(--coral); border-radius: 2px; display: flex; align-items: center; gap: 2px; padding: 0 3px; font-size: 11px; }
  .share i { width: 12px; height: 12px; background: #5877b5; display: inline-block; }
  .share i:nth-child(2) { background: #6fb9dd; } .share i:nth-child(3) { background: #444; } .share i:nth-child(4) { background: #3d6fb0; }
  .share span { margin-left: 3px; }
  .news-heading { margin-top: 14px; font-size: 16px; font-weight: 700; color: var(--heading-grey); }
  .post-title { margin-top: 48px; font-size: 16px; font-weight: 700; color: var(--link-green); line-height: 1.15; }
  .post-meta { font-size: 12.5px; margin-top: 2px; }
  .post-meta b { font-weight: 700; } .post-meta a { color: var(--link-green); font-weight: 700; text-decoration: none; }
  .post-excerpt { margin-top: 24px; font-size: 13.5px; line-height: 1.45; }
  .post-excerpt em { color: var(--link-green); }
  .post-rule { margin-top: 30px; height: 1px; background: var(--rule); }
  .post-title.next { margin-top: 26px; white-space: nowrap; }

  .sidebar { position: absolute; left: 825px; top: 464px; width: 220px; }
  .social { display: flex; gap: 22px; margin-left: 24px; }
  .social i { width: 28px; height: 28px; border-radius: 5px; background: #3b5a9a; display: block; }
  .social i:nth-child(2) { background: #6cc4e9; } .social i:nth-child(3) { background: #c4302b; } .social i:nth-child(4) { background: #f26f21; }
  .ask-box { margin-top: 20px; height: 40px; background: var(--coral); display: flex; align-items: center; gap: 6px; padding-left: 10px; font-family: "Montserrat", sans-serif; color: #fff; }
  .ask-box i { width: 28px; height: 28px; border-radius: 50%; background: var(--slate); color: #fff; font-style: normal; font-size: 12px; display: flex; align-items: center; justify-content: center; }
  .ask-box span { margin-left: 14px; font-size: 18px; letter-spacing: 1px; font-weight: 500; }
  .side-heading { margin-top: 24px; font-size: 16px; font-weight: 700; color: var(--heading-grey); }
  .side-link { display: block; font-size: 11.5px; font-weight: 700; color: var(--link-green); margin-top: 5px; text-decoration: none; }
  .side-link.gap { margin-top: 14px; }
  .forum-box { margin-top: 16px; height: 40px; background: var(--coral); color: #fff; text-align: center; font-family: "Montserrat", sans-serif; font-size: 15px; letter-spacing: 1px; line-height: 1.1; padding-top: 3px; }
</style>
</head>
<body>
  <div class="brand"><span class="brand-dot"></span><span class="brand-name">HAVEN</span></div>

  <form class="search">
    <div class="search-field">Site Search</div>
    <div class="search-button">Search</div>
    <div class="search-clear">×</div>
  </form>

  <nav class="main-nav">
    <div class="nav-tab" style="width:150px">ABOUT HAVEN</div>
    <div class="nav-tab" style="width:152px">ASK US<small>DISCUSSION FORUMS</small></div>
    <div class="nav-tab" style="width:152px">GENERAL<small style="font-size:13.5px">CANCER INFO</small></div>
    <div class="nav-tab" style="width:152px">FOCUSED<small style="font-size:13.5px">CANCER INFO</small></div>
    <div class="nav-tab account" style="width:125px">SIGN IN | JOIN</div>
    <div class="nav-tab donate" style="width:124px"><span class="donate-badge"></span>DONATE</div>
  </nav>

  <section class="lead">
    <div class="lead-photo" role="img" aria-label="Photo of a smiling mother hugging her baby on a soft white blanket"></div>
    <div class="lead-copy">
      <div class="lead-rule"></div>
      <h1 class="lead-title">GIVE TO HAVEN</h1>
      <div class="lead-rule"></div>
      <p class="lead-sub">Cancer patients find answers here.<br>Your donation makes that possible.</p>
    </div>
    <a class="lead-cta">
      <svg width="22" height="24" viewBox="0 0 22 24"><circle cx="11" cy="12" r="10" fill="#fff"/><path d="M11 7v10M6 12h10" stroke="#2db36a" stroke-width="3"/></svg>
      DONATE
    </a>
  </section>

  <main class="news">
    <div class="share"><i></i><i></i><i></i><i></i><span>Share/Email/More</span></div>
    <h2 class="news-heading">Recent HAVEN News &amp; Posts</h2>
    <h3 class="post-title">Cancer Care In Crisis? The Institute of Clinical Policy's Report: Delivering High-Quality Cancer Care: Charting a New Course For a System in Crisis; Part I: The Current Landscape</h3>
    <p class="post-meta">by <b>Dr. Marlow</b> on Nov 10, 2013 in <a>HAVEN :: Cancer Basics</a></p>
    <p class="post-excerpt">&nbsp;A few months ago, the Institute of Clinical Policy released the prepublication proofs of a massive report on the state of oncology care, saying that it was in crisis in the United States. I learned about it from an email that focused on the crisis part of the title. I was bo... &nbsp;<em>(Read More)</em></p>
    <div class="post-rule"></div>
    <h3 class="post-title next">Is there a place for live educational meetings in our new online world? Would</h3>
  </main>

  <aside class="sidebar">
    <div class="social"><i></i><i></i><i></i><i></i></div>
    <div class="ask-box"><i>Q:</i><i>A:</i><span>Ask Us</span></div>
    <h2 class="side-heading">Welcome To HAVEN!</h2>
    <a class="side-link">How To Use HAVEN</a>
    <a class="side-link">General Cancer FAQs</a>
    <a class="side-link gap">Recent HAVEN Site Post Comments</a>
    <div class="forum-box">HAVEN<br>Discussion Forums</div>
    <a class="side-link gap">HAVEN Discussion Forum Guidelines</a>
    <a class="side-link gap">Recent HAVEN Forum Activity</a>
  </aside>
</body>
</html>
```